Business Card Design (NEW FILES)

ATTENTION: New vector files are available. Please update your design to reflect/use the new (better resolution) logo images.

Seeking a unique and professional business card design for a commercial drone photography/videography business. The layout should feature
the logo (attached) and include the following information:
978-512-6037
www.skyvantmedia.com
ORD Certified Remote Pilot

```html
<!DOCTYPE html>
<html lang="en">
<head>
<meta charset="utf-8">
<title>Skyvant Media – Business Card</title>
<link href="https://fonts.googleapis.com/css2?family=Montserrat:wght@400;500&display=swap" rel="stylesheet">
<style>
  :root {
    --backdrop: #7a7fa8;
    --navy: #171a4a;
    --ink: #1c1f4f;
    --orange: #ef8a3c;
    --paper: #ffffff;
  }
  * { margin: 0; padding: 0; box-sizing: border-box; }
  html, body {
    width: 1200px; height: 876px; overflow: hidden;
    background: var(--backdrop);
    font-family: "Montserrat", Arial, sans-serif;
  }
  .stage {
    width: 1200px; height: 876px;
    display: flex; align-items: center; justify-content: center; gap: 40px;
  }
  .card {
    width: 520px; height: 298px;
    position: relative;
    box-shadow: 0 6px 18px rgba(20, 22, 60, 0.25);
  }
  .card--front { background: var(--paper); }
  .card--back { background: var(--navy); display: flex; align-items: center; justify-content: center; }

  .contact { position: absolute; left: 34px; top: 38px; }
  .contact__name {
    font-weight: 500; font-size: 19px; letter-spacing: 0.5px;
    color: var(--ink); text-transform: uppercase; line-height: 24px;
  }
  .contact__role { font-size: 12px; color: var(--orange); margin-top: 2px; line-height: 16px; }
  .contact__list { list-style: none; margin-top: 12px; }
  .contact__item {
    display: flex; align-items: center; gap: 8px;
    font-size: 12.5px; color: var(--ink); line-height: 20px;
  }
  .contact__item svg { width: 11px; height: 11px; fill: var(--orange); flex: none; }

  .wordmark {
    display: flex; align-items: center; gap: 10px;
    font-weight: 500; text-transform: uppercase; letter-spacing: 1px;
    white-space: nowrap;
  }
  .wordmark__dot { border-radius: 50%; background: var(--orange); flex: none; }
  .card--front .wordmark {
    position: absolute; right: 40px; top: 196px;
    color: var(--ink); font-size: 21px;
  }
  .card--front .wordmark__dot { width: 13px; height: 13px; }
  .card--back .wordmark { color: var(--paper); font-size: 32px; }
  .card--back .wordmark__dot { width: 18px; height: 18px; }
</style>
</head>
<body>
<main class="stage">
  <section class="card card--front" aria-label="Business card front">
    <div class="contact">
      <h1 class="contact__name">Mark Doyle</h1>
      <p class="contact__role">Owner</p>
      <ul class="contact__list">
        <li class="contact__item">
          <svg viewBox="0 0 24 24" aria-hidden="true"><path d="M6.6 10.8a15.1 15.1 0 0 0 6.6 6.6l2.2-2.2a1 1 0 0 1 1-.25 11.4 11.4 0 0 0 3.6.57 1 1 0 0 1 1 1V20a1 1 0 0 1-1 1A17 17 0 0 1 3 4a1 1 0 0 1 1-1h3.5a1 1 0 0 1 1 1c0 1.25.2 2.45.57 3.57a1 1 0 0 1-.25 1z"/></svg>
          978-512-6037
        </li>
        <li class="contact__item">
          <svg viewBox="0 0 24 24" aria-hidden="true"><path d="M2 5h20v14H2z M3.5 6.5 12 13l8.5-6.5" stroke="#fff" stroke-width="1.5"/></svg>
          md@skyvantmedia.com
        </li>
        <li class="contact__item">
          <svg viewBox="0 0 24 24" aria-hidden="true"><circle cx="12" cy="12" r="10"/><path d="M2 12h20M12 2c3 3 3 17 0 20M12 2c-3 3-3 17 0 20" stroke="#fff" stroke-width="1.3" fill="none"/></svg>
          www.skyvantmedia.com
        </li>
        <li class="contact__item">
          <svg viewBox="0 0 24 24" aria-hidden="true"><circle cx="12" cy="12" r="10"/><path d="M7 12.5l3.2 3.2L17 9" stroke="#fff" stroke-width="2.2" fill="none"/></svg>
          ORD Certified Remote Pilot
        </li>
      </ul>
    </div>
    <div class="wordmark">
      <span class="wordmark__dot" aria-hidden="true"></span>
      <span>Skyvant Media</span>
    </div>
  </section>

  <section class="card card--back" aria-label="Business card back">
    <div class="wordmark">
      <span class="wordmark__dot" aria-hidden="true"></span>
      <span>Skyvant Media</span>
    </div>
  </section>
</main>
</body>
</html>
```